A modern, fresh introduction to Buddhism

I need a book cover for an A6 sized book to be used both for ebook and hard copy. The author is a young, modern Buddhist teacher of high standing who has written this short intro to Buddhism in an informal Q & As format using modern, accessible language to convey profound and meaningful ideas to the general public. The author is Tibetan, but teaches worldwide and is very personable and dynamic. The cover should portray this and have a fresh yet authentic feel to it (nothing new-agey!). Please see the author's websites www.norvalemtasheteacher.org and www.pwrt.org for reference, but do not feel that the design must align completely with the website designs.

Target Market(s)

General public both in Europe and America and in Asia ranging from teenagers to the elderly. A really broad audience.

Industry/Entity Type

Teacher

Requirements
Must have
• Please include the following text that on the front cover:

A Window onto Stillness

By Drawa Tsomen Lhundrup

Please include the following on the back cover:

Yunor Trenpa Publications (with attached logo above it)
Nice to have
• A simplistic, artistic, and modern look without any traditional religious images.
Should not have
• No buddha images or religious images. I would prefer a more simplistic, modern and artistic look.

```html
<!DOCTYPE html>
<html lang="en">
<head>
<meta charset="utf-8">
<title>A Window onto Stillness — Book Cover</title>
<link rel="stylesheet" href="https://fonts.googleapis.com/css2?family=Cinzel:wght@400;500&family=Open+Sans:wght@400&display=swap">
<style>
  :root {
    --page-bg: #ffffff;
    --petal-deep: #e0661a;
    --petal-orange: #f08a1c;
    --petal-gold: #f7b526;
    --petal-yellow: #fbd64a;
    --glow-cream: #fdf2c0;
    --glow-white: #fffbe6;
    --title-colour: #b04a22;
    --author-colour: #6e4e2c;
  }

  html, body {
    margin: 0;
    padding: 0;
    width: 1011px;
    height: 1200px;
    overflow: hidden;
    background: var(--page-bg);
  }

  .canvas {
    position: relative;
    width: 1011px;
    height: 1200px;
  }

  .book-cover {
    position: absolute;
    left: 126px;
    top: 64px;
    width: 760px;
    height: 1072px;
    overflow: hidden;
    box-shadow: 0 2px 10px rgba(0, 0, 0, 0.18);
  }

  .cover-photo {
    position: absolute;
    inset: 0;
    background:
      radial-gradient(ellipse 70% 45% at 48% 62%, var(--glow-white) 0%, var(--glow-cream) 35%, rgba(253, 242, 192, 0) 75%),
      linear-gradient(180deg, var(--petal-deep) 0%, var(--petal-orange) 18%, var(--petal-gold) 38%, var(--petal-yellow) 58%, var(--glow-cream) 80%, var(--petal-yellow) 100%);
  }

  .cover-text {
    position: absolute;
    left: 0;
    right: 0;
    top: 770px;
    text-align: center;
  }

  .book-title {
    margin: 0;
    font-family: "Cinzel", "Times New Roman", serif;
    font-weight: 400;
    font-size: 62px;
    line-height: 1.05;
    letter-spacing: 0.01em;
    color: var(--title-colour);
    text-shadow: 0 1px 3px rgba(255, 255, 255, 0.6);
  }

  .book-author {
    margin: 34px 0 0;
    font-family: "Open Sans", Arial, sans-serif;
    font-size: 24px;
    color: var(--author-colour);
  }
</style>
</head>
<body>
  <main class="canvas">
    <section class="book-cover">
      <div class="cover-photo" role="img" aria-label="Close-up photograph of bright orange and yellow flower petals hanging down against a glowing pale yellow light"></div>
      <div class="cover-text">
        <h1 class="book-title">A Window<br>onto Stillness</h1>
        <p class="book-author">Drawa Tsomen Lhundrup</p>
      </div>
    </section>
  </main>
</body>
</html>
```